Business card design for Velvet Harbor

We need business cards designed for our new marketing consulting company, Velvet Harbor. Our services include marketing strategy, go-to-market and launch planning, growth strategy, and execution. We serve medical technology and health technology companies, from startups to well-established growth companies.

The business cards should feel professional, credible, reliable and trustworthy, and should instill confidence. Also bold, creative, and modern.

The design must use the Velvet Harbor logo.

The primary brand color is this orange: #FF5501
A secondary color that you can use is this gray: #282B2D
I would prefer only to use the orange and gray. But if you feel you really need an additional accent color (please use it very sparingly, as little as possible), you can use this blue for small accent purposes: #009FED

Attached are the logo files. The main logo is the one with a little bit of orange on the left and the rest is gray.

The business card should include the following:

Velvet Harbor logo
First name and last name
Title
Email address
Phone number and type (in whatever order looks best for the design
Website (the website does not need to be in the same block as the personal info)

For example:

Nessa Pryle
Founder & Principal
nessa@velvetharbor.com
+1.628.309.4156 mobile (can use "." or spaces in between blocks of numbers)
velvetharbor.com (somewhere on the card, it does not need to be with the personal info; and note that there is no "www." at the beginning)

Note that there will be no address listed on the business card.

Target Market(s)

Executives (CEO, head of marketing, head of sales) at medical technology and health technology companies, mostly in their 40s and older, well-educated, often with advanced degrees. They are strategic thinkers, responsible for budgets, and familiar with P&L. Their comfort with and trust in using outside consultants varies.

Industry/Entity Type

Medical technology and health technology companies.

Contact Information for Business Card

See project description

Font styles to use
Sans Serif

Requirements
Must have
• Logo and see Business card details section above.

```html
<!DOCTYPE html>
<html lang="en">
<head>
<meta charset="utf-8">
<title>Velvet Harbor — Business Card</title>
<link rel="stylesheet" href="https://fonts.googleapis.com/css2?family=Michroma&family=Montserrat:wght@400;500&display=swap">
<style>
  :root {
    --orange: #FF5501;
    --gray: #282B2D;
    --ink: #1f2123;
    --paper: #f4f4f2;
    --back-card: #1b1c1e;
    --back-mark: #3b3e41;
    --stage: #1a1a1b;
    --muted: #9a9b9d;
  }
  * { box-sizing: border-box; margin: 0; padding: 0; }
  html, body { width: 1200px; height: 852px; overflow: hidden; }
  body {
    background: var(--stage);
    display: flex;
    align-items: center;
    justify-content: center;
    gap: 40px;
    font-family: "Montserrat", sans-serif;
  }
  .card {
    position: relative;
    width: 520px;
    height: 297px;
    border-radius: 18px;
    overflow: hidden;
    box-shadow: 0 14px 30px rgba(0,0,0,.45);
  }

  /* Back side */
  .card-back {
    background: var(--back-card);
    display: flex;
    flex-direction: column;
    align-items: center;
    justify-content: center;
    gap: 22px;
  }
  .back-brand {
    display: flex;
    align-items: center;
    gap: 16px;
  }
  .back-dot {
    width: 34px; height: 34px;
    border-radius: 50%;
    background: var(--back-mark);
  }
  .back-name {
    font-family: "Michroma", sans-serif;
    font-size: 26px;
    letter-spacing: 3px;
    color: var(--back-mark);
    text-transform: uppercase;
  }
  .back-web {
    font-size: 13px;
    color: #d8d8d8;
    letter-spacing: .3px;
  }

  /* Front side */
  .card-front { background: var(--paper); }
  .front-shape { position: absolute; inset: 0; }
  .front-brand {
    position: absolute;
    left: 30px;
    bottom: 48px;
    display: flex;
    align-items: center;
    gap: 10px;
  }
  .brand-dot {
    width: 18px; height: 18px;
    border-radius: 50%;
    background: var(--gray);
  }
  .brand-name {
    font-family: "Michroma", sans-serif;
    font-size: 15px;
    letter-spacing: 2px;
    color: var(--gray);
    text-transform: uppercase;
  }
  .contact-block {
    position: absolute;
    left: 330px;
    top: 78px;
  }
  .person-name {
    font-family: "Michroma", sans-serif;
    font-size: 18px;
    letter-spacing: 1.5px;
    color: var(--ink);
    text-transform: uppercase;
  }
  .person-title {
    font-size: 12px;
    font-weight: 500;
    color: var(--orange);
    margin-top: 3px;
  }
  .contact-list {
    list-style: none;
    margin-top: 20px;
    display: grid;
    gap: 6px;
  }
  .contact-item {
    display: flex;
    align-items: center;
    gap: 8px;
    font-size: 11px;
    color: var(--ink);
  }
  .contact-icon { width: 10px; height: 10px; flex: none; }
</style>
</head>
<body>

  <section class="card card-back" aria-label="Card back">
    <div class="back-brand">
      <span class="back-dot"></span>
      <span class="back-name">Velvet Harbor</span>
    </div>
    <p class="back-web">velvetharbor.com</p>
  </section>

  <section class="card card-front" aria-label="Card front">
    <svg class="front-shape" viewBox="0 0 520 297" width="520" height="297">
      <path d="M0 0 H258 Q340 150 280 297 H0 Z" fill="var(--gray)"/>
      <path d="M0 0 H244 Q326 150 266 297 H0 Z" fill="var(--orange)"/>
    </svg>

    <div class="front-brand">
      <span class="brand-dot"></span>
      <span class="brand-name">Velvet Harbor</span>
    </div>

    <div class="contact-block">
      <h1 class="person-name">Nessa Pryle</h1>
      <p class="person-title">Founder &amp; Principal</p>
      <ul class="contact-list">
        <li class="contact-item">
          <svg class="contact-icon" viewBox="0 0 10 10"><path d="M2 0.5 L4 2.5 L3 3.8 Q4.5 6 6.2 7 L7.5 6 L9.5 8 L8 9.5 Q3 9 0.5 2 Z" fill="var(--orange)"/></svg>
          +1.628.309.4156
        </li>
        <li class="contact-item">
          <svg class="contact-icon" viewBox="0 0 10 10"><rect x="0.5" y="2" width="9" height="6.5" fill="var(--orange)"/><path d="M0.5 2 L5 5.8 L9.5 2" fill="none" stroke="#fff" stroke-width="0.8"/></svg>
          nessa@velvetharbor.com
        </li>
        <li class="contact-item">
          <svg class="contact-icon" viewBox="0 0 10 10"><circle cx="5" cy="5" r="4.5" fill="var(--orange)"/><path d="M0.5 5 H9.5 M5 0.5 V9.5 M5 0.5 Q2 5 5 9.5 M5 0.5 Q8 5 5 9.5" fill="none" stroke="#fff" stroke-width="0.6"/></svg>
          velvetharbor.com
        </li>
      </ul>
    </div>
  </section>

</body>
</html>
```